Business Card Design Project

We need a simple business card design that uses our current logo.
We need to have the current logo put into a high res format.
We need to have 1 card made with contact information.
We will supply the information for the 4 employees.
Industry/Entity Type
Business
Requirements
Must have
- The contact information is as follows:
Mark Dellweather
Producer/CEO
c. 949-555-0147
f. 650-555-0193
markd@lanternbay.example
Al Vostrand, CFO
c. 949-555-0162
f. 650-555-0193
alv@lanternbay.example
Peter Malvane, PR
c. 267-555-0128
f. 650-555-0193
pmalvane@lanternbay.example
Tim Garrowby, Producer
c. 949-555-0184
f. 650-555-0193
timg@lanternbay.example
The address for all cards is:
318 W Calle Norvento #2715, San Clemente, CA 92681

```html
<!DOCTYPE html>
<html lang="en">
<head>
<meta charset="utf-8">
<title>Lantern Bay Media — Business Card</title>
<link rel="stylesheet" href="https://fonts.googleapis.com/css2?family=Open+Sans:wght@300;400;700&display=swap">
<style>
  :root {
    --ink-top: #15191c;
    --ink-deep: #030405;
    --band-dark: #103a5c;
    --band-mid: #1f6db0;
    --band-glow: #3a9be6;
    --brand-blue: #56aef0;
    --text-white: #ffffff;
    --outline: #000000;
  }
  * { margin: 0; padding: 0; box-sizing: border-box; }
  html, body {
    width: 1200px;
    height: 1000px;
    overflow: hidden;
    background: var(--ink-deep);
  }
  .card {
    position: relative;
    width: 1200px;
    height: 1000px;
    overflow: hidden;
    font-family: "Open Sans", sans-serif;
    background: linear-gradient(
      to bottom,
      var(--ink-top) 0px,
      #12171b 250px,
      #0f2436 310px,
      var(--band-dark) 350px,
      var(--band-mid) 388px,
      var(--band-glow) 400px,
      var(--band-mid) 414px,
      var(--band-dark) 470px,
      #0a1f30 530px,
      #050b10 600px,
      var(--ink-deep) 660px,
      var(--ink-deep) 1000px
    );
  }
  .glow-line {
    position: absolute;
    left: 0;
    top: 394px;
    width: 1200px;
    height: 14px;
    background: linear-gradient(to bottom, transparent, rgba(90,175,245,0.75), transparent);
  }
  .brand-name {
    position: absolute;
    left: 52px;
    top: 208px;
    font-weight: 700;
    font-size: 88px;
    line-height: 1;
    letter-spacing: 0;
    color: var(--brand-blue);
    white-space: nowrap;
  }
  .address {
    position: absolute;
    left: 106px;
    top: 393px;
    font-style: normal;
    font-weight: 400;
    font-size: 46px;
    line-height: 52px;
    color: var(--text-white);
    text-shadow:
      -2px -2px 0 var(--outline), 2px -2px 0 var(--outline),
      -2px 2px 0 var(--outline), 2px 2px 0 var(--outline),
      0 -2px 0 var(--outline), 0 2px 0 var(--outline),
      -2px 0 0 var(--outline), 2px 0 0 var(--outline);
    white-space: nowrap;
  }
  .contact {
    position: absolute;
    left: 545px;
    top: 628px;
    font-weight: 300;
    font-size: 47px;
    line-height: 50px;
    color: var(--text-white);
    white-space: nowrap;
  }
</style>
</head>
<body>
  <main class="card">
    <div class="glow-line"></div>
    <h1 class="brand-name">LANTERN BAY MEDIA</h1>
    <address class="address">
      318 W Calle Norvento #2715<br>
      San Clemente, CA&nbsp; 92681
    </address>
    <div class="contact">
      <div class="contact-name">Mark Dellweather</div>
      <div class="contact-title">Producer/CEO</div>
      <div class="contact-cell">c. 949-555-0147</div>
      <div class="contact-fax">f. 650-555-0193</div>
      <div class="contact-email">markd@lanternbay.example</div>
    </div>
  </main>
</body>
</html>
```